Boutique raw honey label from Australia. Blue mountains clean environment

I need a quirky Eco label for a raw honey product to appeal to boutique honey buyers with Gm free 100% raw honey included. Honey come from blue mountains a world heritage listed area in nsw Aust.
Want to appeal to people who love good food and love beautiful things and who want to know where there food comes from and how it is grown. Gm free, pesticide free, hand poured family run and owned business

Target Market(s)

Health conscious, lovers of fine food

Industry/Entity Type

Environment

Other font styles liked:
• Courier

Requirements
Must have
• 100% Raw
Nice to have
• A little blurb about where honey is from
• # please see my current label - something similar to this but with a vintage bee design possibly

```html
<!DOCTYPE html>
<html lang="en">
<head>
<meta charset="utf-8">
<title>Wild Ridge Honey co. – Raw Honey Label</title>
<link rel="stylesheet" href="https://fonts.googleapis.com/css2?family=Courier+Prime:wght@400;700&display=swap">
<style>
  :root {
    --label-black: #000000;
    --honey-gold: #8a7650;
    --dot-gold: #9a8558;
    --paper-white: #ffffff;
    --comb-light: #f6d64a;
    --comb-mid: #e9bc1c;
    --comb-deep: #c99a08;
  }
  html, body {
    margin: 0;
    padding: 0;
    overflow: hidden;
    background: var(--label-black);
  }
  .label {
    position: relative;
    width: 1200px;
    height: 946px;
    background: var(--label-black);
    overflow: hidden;
    font-family: "Courier Prime", "Courier New", monospace;
    color: var(--paper-white);
  }
  .label-art {
    position: absolute;
    inset: 0;
  }
  .brand-name {
    position: absolute;
    left: 0;
    right: 0;
    top: 128px;
    margin: 0;
    text-align: center;
    font-family: "Courier Prime", "Courier New", monospace;
    font-weight: 700;
    font-size: 70px;
    line-height: 1;
    color: var(--honey-gold);
    letter-spacing: 0;
    white-space: nowrap;
  }
  .origin-blurb {
    position: absolute;
    left: 0;
    top: 0;
    margin: 0;
    width: 1200px;
  }
  .origin-blurb .line-one {
    position: absolute;
    left: 108px;
    top: 244px;
    white-space: nowrap;
    font-size: 35px;
    line-height: 1;
  }
  .origin-blurb .raw-claim {
    font-size: 45px;
  }
  .origin-blurb .line-two {
    position: absolute;
    left: 207px;
    top: 310px;
    white-space: nowrap;
    font-size: 33px;
    line-height: 1;
  }
  .origin-blurb .region {
    font-weight: 700;
  }
  .claims {
    position: absolute;
    left: 107px;
    top: 804px;
    margin: 0;
    font-size: 26px;
    line-height: 1;
    white-space: nowrap;
    display: flex;
    align-items: center;
    gap: 14px;
  }
  .claims .hex-bullet {
    width: 18px;
    height: 20px;
    display: inline-block;
  }
  .net-weight {
    position: absolute;
    right: 100px;
    top: 806px;
    margin: 0;
    font-size: 25px;
    line-height: 1;
    white-space: nowrap;
  }
</style>
</head>
<body>
<main class="label">
  <svg class="label-art" width="1200" height="946" viewBox="0 0 1200 946">
    <defs>
      <radialGradient id="comb-fill" cx="0.45" cy="0.4" r="0.7">
        <stop offset="0" stop-color="var(--comb-light)"/>
        <stop offset="0.6" stop-color="var(--comb-mid)"/>
        <stop offset="1" stop-color="var(--comb-deep)"/>
      </radialGradient>
    </defs>

    <g class="dotted-rules" stroke="var(--dot-gold)" stroke-width="2" stroke-dasharray="1.5 4.5" stroke-linecap="round">
      <line x1="0" y1="44" x2="1200" y2="44"/>
      <line x1="0" y1="76" x2="1200" y2="76"/>
      <line x1="0" y1="868" x2="1200" y2="868"/>
      <line x1="0" y1="900" x2="1200" y2="900"/>
    </g>

    <g class="comb-frames" fill="none" stroke="var(--honey-gold)" stroke-width="2">
      <polygon class="side-cell-outer" points="254,431 397,511 397,670 254,749 111,670 111,511"/>
      <polygon class="side-cell-inner" points="254,449 382,520 382,661 254,731 126,661 126,520"/>
      <polygon class="side-cell-outer" points="946,431 1089,511 1089,670 946,749 803,670 803,511"/>
      <polygon class="side-cell-inner" points="946,449 1074,520 1074,661 946,731 818,661 818,520"/>
      <polygon class="centre-cell-outer" points="600,366 803,478 803,702 600,814 397,702 397,478"/>
    </g>

    <g class="centre-cell-art" role="img" aria-label="Vintage engraved honey bee illustration on a golden honeycomb background">
      <polygon points="600,389 781,490 781,691 600,791 419,691 419,490" fill="url(#comb-fill)" stroke="var(--honey-gold)" stroke-width="2"/>
    </g>
  </svg>

  <h1 class="brand-name">Wild Ridge Honey co.</h1>

  <p class="origin-blurb">
    <span class="line-one"><span class="raw-claim">100% raw honey</span> hand-poured in the</span>
    <span class="line-two"><span class="region">Blue Mountains</span> of New South Wales Australia.</span>
  </p>

  <p class="claims">
    <span>GM free</span>
    <svg class="hex-bullet" viewBox="0 0 18 20" aria-hidden="true">
      <polygon points="9,0 18,5 18,15 9,20 0,15 0,5" fill="var(--honey-gold)"/>
    </svg>
    <span>pesticide free</span>
  </p>

  <p class="net-weight">Net wt. 430 gr</p>
</main>
</body>
</html>
```